bottle label/ product label for smoothies (ultra fresh)

Please create a bottle label for our smoothies for retail distribution.
It's important that the following key features are clearly stated:

Ultra-fresh

Handmade

No preservatives

Not heat-treated

No added sugar

The base of the product label should be transparent, so that the color and content of the smoothie can be seen clearly.

We are a young, dynamic company. Our values are honesty, ultra-freshness, and authenticity — and we are the only ones producing this type of product in our country. We are positioned in the premium segment.

Design style: Modern, clean, and natural — but not playful or childish.

Example product: Kelu Kelu (Mango, Pineapple, Lemon, Passion Fruit, Orange)

Wenn du möchtest, kann ich auch gleich einen konkreten Vorschlag für das Etikettendesign auf Englisch oder einen Entwurfstext für das Label selbst erstellen. Sag einfach Bescheid!

Target Market(s)

trade - convenience

Industry/Entity Type

trade

Font styles to use
Sans Serif

Requirements
Must have
• sales- features: Ultra-fresh Handmade No preservatives Not heat-treated No added sugar

```html
<!DOCTYPE html>
<html lang="en">
<head>
<meta charset="utf-8">
<title>olvina smoothie labels</title>
<link rel="stylesheet" href="https://fonts.googleapis.com/css2?family=Nunito:wght@700;800&family=Barlow+Condensed:wght@500&family=Archivo:wght@400;700&display=swap">
<style>
  :root {
    --page: #ffffff;
    --ink: #ffffff;
    --pineapple-top: #c7a418;
    --pineapple-panel-a: #e2ae0c;
    --pineapple-panel-b: #f6f300;
    --lemon-top: #93c314;
    --lemon-panel-a: #126613;
    --lemon-panel-b: #80be1c;
    --mango-top: #c1531b;
    --mango-panel-a: #e37a2c;
    --mango-panel-b: #f5400a;
  }
  * { margin: 0; padding: 0; box-sizing: border-box; }
  html, body { width: 1200px; height: 807px; overflow: hidden; background: var(--page); }
  .range {
    position: relative;
    width: 1200px; height: 807px;
  }
  .label {
    position: absolute;
    top: 212px;
    width: 152px; height: 384px;
    border-radius: 6px;
    overflow: hidden;
    color: var(--ink);
    background: var(--top);
  }
  .label--pineapple { left: 314px; --top: var(--pineapple-top); --pa: var(--pineapple-panel-a); --pb: var(--pineapple-panel-b); }
  .label--lemon { left: 516px; --top: var(--lemon-top); --pa: var(--lemon-panel-a); --pb: var(--lemon-panel-b); }
  .label--mango { left: 718px; --top: var(--mango-top); --pa: var(--mango-panel-a); --pb: var(--mango-panel-b); }

  .claim {
    position: absolute; top: 12px; width: 100%;
    text-align: center;
    font: 800 12px/1 "Nunito", sans-serif;
    opacity: .82;
    letter-spacing: .2px;
  }
  .brand {
    position: absolute; top: 70px; width: 100%;
    text-align: center;
    font: 800 30px/1 "Nunito", sans-serif;
    letter-spacing: .3px;
  }
  .flavour {
    position: absolute; top: 142px; left: 7px;
    font: 500 26px/1 "Barlow Condensed", sans-serif;
    letter-spacing: .4px;
    padding-bottom: 2px;
    border-bottom: 3px solid var(--ink);
  }
  .panel {
    position: absolute; top: 174px; left: 0;
    width: 100%; height: 210px;
    background: linear-gradient(to top right, var(--pb) 0%, var(--pa) 100%);
  }
  .features {
    list-style: none;
    position: absolute; top: 6px; left: 7px;
    font: 400 6.4px/10.5px "Archivo", sans-serif;
    letter-spacing: .6px;
    text-transform: uppercase;
  }
  .features b { font-weight: 700; }
  .volume {
    position: absolute; left: 8px; bottom: 24px;
    font: 400 13px/1 "Archivo", sans-serif;
    padding-bottom: 3px;
  }
  .volume small { font-size: 8px; }
  .volume::after {
    content: ""; position: absolute; left: 0; bottom: -3px;
    width: 20px; height: 2.5px; background: var(--ink);
  }
  .handmade {
    position: absolute; left: 8px; bottom: 12px;
    font: 700 5px/1 "Archivo", sans-serif;
    letter-spacing: .8px;
  }
</style>
</head>
<body>
<main class="range">
  <article class="label label--pineapple">
    <p class="claim">No added sugar</p>
    <p class="brand">olvina</p>
    <h2 class="flavour">PINEAPPLE</h2>
    <section class="panel">
      <ul class="features">
        <li><b>Ultra</b>-fresh</li>
        <li><b>Not heat</b>-treated</li>
        <li><b>No</b> preservatives</li>
      </ul>
      <p class="volume">200<small>ml</small></p>
      <p class="handmade">HANDMADE</p>
    </section>
  </article>

  <article class="label label--lemon">
    <p class="claim">No added sugar</p>
    <p class="brand">olvina</p>
    <h2 class="flavour">LEMON</h2>
    <section class="panel">
      <ul class="features">
        <li><b>Ultra</b>-fresh</li>
        <li><b>Not heat</b>-treated</li>
        <li><b>No</b> preservatives</li>
      </ul>
      <p class="volume">200<small>ml</small></p>
      <p class="handmade">HANDMADE</p>
    </section>
  </article>

  <article class="label label--mango">
    <p class="claim">No added sugar</p>
    <p class="brand">olvina</p>
    <h2 class="flavour">MANGO</h2>
    <section class="panel">
      <ul class="features">
        <li><b>Ultra</b>-fresh</li>
        <li><b>Not heat</b>-treated</li>
        <li><b>No</b> preservatives</li>
      </ul>
      <p class="volume">200<small>ml</small></p>
      <p class="handmade">HANDMADE</p>
    </section>
  </article>
</main>
</body>
</html>
```